New Website Design for Rides for Heroes.org - A Site for People to Donate Cars to War / Disabled Ve

Current site: www.ridesforheroes.org; Look at these sites for ideas: bykes2tots.org; motorsfordreams.org; www.autosforourcadets.org; www.trucksforheroes.org

Industry/Entity Type

Charity

Coding

Coded - Design and coding required

Number of Pages Required

1 page

Requirements
Must have
• n/a
Nice to have
• n/a
Should not have
• n/a

```html
<!DOCTYPE html>
<html lang="en">
<head>
<meta charset="utf-8">
<title>Rides For Heroes – Donate Your Car</title>
<link href="https://fonts.googleapis.com/css2?family=Open+Sans:wght@400;600;700;800&display=swap" rel="stylesheet">
<style>
:root{
  --navy:#0f2f86;
  --navy-dark:#0a2470;
  --royal:#1d4aa3;
  --cyan:#3ec3ee;
  --red:#e11f26;
  --ink:#1b1b1b;
  --heading:#0d2a80;
  --panel:rgba(246,246,248,.93);
  --frame:#e6e6e6;
  --white:#ffffff;
}
*{box-sizing:border-box;margin:0;padding:0}
html,body{width:1200px;height:2375px;overflow:hidden}
body{background:var(--frame);font-family:"Open Sans",Arial,sans-serif;color:var(--ink);position:relative}
.page{position:absolute;left:16px;top:16px;width:1168px;height:2343px;background:var(--white)}
.header{position:absolute;left:0;top:0;width:1168px;height:149px;
  background:linear-gradient(100deg,#3d4456 0%,#6f7282 30%,#a9a8b4 48%,#b33a45 62%,#d9d5da 74%,#9f2b38 88%,#7b2330 100%)}
.brand{position:absolute;left:30px;top:46px;display:flex;align-items:center;gap:14px}
.brand-dot{width:46px;height:46px;border-radius:50%;background:var(--red)}
.brand-name{font-weight:800;font-size:30px;color:var(--white);letter-spacing:.5px;text-transform:uppercase}
.helpline{position:absolute;right:22px;top:28px;text-align:center;color:var(--white);font-weight:700;line-height:1}
.helpline .ask{font-size:19px}
.helpline .call{font-size:28px;margin-top:5px}
.helpline .hours{font-size:19px;margin-top:4px;line-height:21px}
.nav{position:absolute;left:0;top:149px;width:1168px;height:49px;background:var(--navy);display:flex;justify-content:center;align-items:center;gap:50px}
.nav a{color:var(--white);text-decoration:none;font-weight:700;font-size:20px}
.backdrop{position:absolute;left:0;top:198px;width:1168px;height:1880px;
  background:linear-gradient(170deg,#27427f 0%,#4a66a8 18%,#c9cfe0 34%,#b8343f 46%,#e7e1e3 56%,#a82b37 66%,#dcdadf 76%,#5a6f3c 90%,#3c5029 100%)}
.hero-photo{position:absolute;left:49px;top:248px;width:649px;height:496px;
  background:linear-gradient(180deg,#3a2b14 0%,#8a6a2e 40%,#d8b865 62%,#5a4418 82%,#1e160a 100%)}
.hero-title{position:absolute;left:49px;top:636px;width:649px;text-align:center;color:var(--white);font-weight:700;font-size:34px;line-height:37px;text-transform:uppercase}
.form-panel{position:absolute;left:719px;top:248px;width:398px;height:496px;background:var(--navy);text-align:center;padding-top:30px}
.form-panel h2{color:var(--cyan);font-size:27px;font-weight:700;text-transform:uppercase}
.form-panel .lead{color:var(--white);font-weight:700;font-size:15px;line-height:20px;margin-top:10px}
.fields{position:absolute;left:29px;top:154px;width:341px;display:grid;grid-template-columns:1fr 1fr;gap:10px}
.field{height:35px;border:1.5px solid #c9d4f0;border-radius:3px;color:var(--white);font-size:14px;font-weight:600;text-align:left;padding:8px 12px;position:relative}
.field.wide{grid-column:1 / 3}
.field .caret{position:absolute;right:10px;top:13px;width:0;height:0;border-left:6px solid transparent;border-right:6px solid transparent;border-top:7px solid var(--white)}
.donate-btn{position:absolute;left:118px;top:446px;width:166px;height:33px;background:var(--red);color:var(--white);font-weight:700;font-size:15px;line-height:33px;text-transform:uppercase}
.panel{position:absolute;left:49px;width:1068px;background:var(--panel);text-align:center}
.panel h2{color:var(--heading);font-weight:700;font-size:26px;text-transform:uppercase}
.steps{top:774px;height:362px;padding-top:26px}
.step{position:absolute;top:80px;width:260px;text-align:center}
.step-disc{width:190px;height:190px;border-radius:50%;border:3px solid var(--royal);padding:5px;margin:0 auto}
.step-disc span{display:block;width:100%;height:100%;border-radius:50%;background:radial-gradient(circle,#3b5db0 0%,var(--royal) 70%)}
.step p{font-weight:700;font-size:15px;line-height:21px;margin-top:14px;text-transform:uppercase}
.reasons{top:1168px;height:348px;padding-top:26px}
.reasons ul{list-style:none;text-align:left;position:absolute;left:49px;top:82px}
.reasons li{display:flex;align-items:center;gap:14px;height:34.7px;font-size:15px}
.reasons li b{font-weight:700}
.arrow-dot{width:26px;height:26px;flex:none}
.today{top:1548px;height:478px;padding-top:26px}
.perk{position:absolute;top:84px;width:200px}
.perk-disc{width:142px;height:142px;border-radius:50%;border:2.5px solid var(--royal);padding:4px;margin:0 auto}
.perk-disc div{width:100%;height:100%;border-radius:50%;background:var(--royal);display:flex;align-items:center;justify-content:center}
.perk p{font-weight:600;font-size:16px;line-height:21px;margin-top:12px}
.secure-title{position:absolute;left:0;width:100%;top:332px}
.badges{position:absolute;left:0;width:100%;top:398px;display:flex;justify-content:center;align-items:center;gap:40px}
.badge-rect{width:170px;height:54px;background:#1f5b73;border:2px solid #111}
.badge-round{width:58px;height:58px;border-radius:50%;border:3px dashed #3a8fc7}
.badge-shield{width:124px;height:38px;background:#d9d9d9}
.footer{position:absolute;left:0;top:2078px;width:1168px;height:225px;
  background:linear-gradient(100deg,var(--navy-dark) 0%,var(--navy) 62%,#2a3f80 78%,#8a2a3a 100%);color:var(--white)}
.footer h3{font-size:14px;font-weight:700;color:#c9d3f2;margin-bottom:12px}
.foot-about{position:absolute;left:66px;top:34px;width:260px}
.foot-about p{font-size:12.5px;font-weight:600;line-height:19px}
.foot-nav{position:absolute;left:372px;top:34px}
.foot-nav a{display:block;color:var(--white);text-decoration:none;font-size:13px;font-weight:600;line-height:21px}
.foot-contact{position:absolute;left:514px;top:34px}
.foot-contact .line{display:flex;gap:12px;font-weight:700;font-size:14px;line-height:20px}
.foot-brand{position:absolute;right:64px;top:98px;display:flex;align-items:center;gap:12px}
.foot-brand .brand-dot{width:36px;height:36px}
.foot-brand .brand-name{font-size:23px}
.copyright{position:absolute;left:0;top:2303px;width:1168px;height:40px;background:var(--white);text-align:center;font-size:12px;font-weight:700;line-height:40px;text-transform:uppercase}
</style>
</head>
<body>
<div class="page">
  <header class="header" role="img" aria-label="Waving American flag banner behind the header">
    <div class="brand"><span class="brand-dot"></span><span class="brand-name">Rides For Heroes</span></div>
    <div class="helpline">
      <div class="ask">WE NEED YOUR HELP</div>
      <div class="call">CALL 1-800-555-0142</div>
      <div class="hours">Live Operators Available<br>7 Days A Week</div>
    </div>
  </header>
  <nav class="nav">
    <a href="#">HOW TO DONATE</a><a href="#">WHY DONATE</a><a href="#">FAQ</a><a href="#">ABOUT</a>
  </nav>

  <div class="backdrop" role="img" aria-label="Background photo of American flags waving over a green field"></div>

  <div class="hero-photo" role="img" aria-label="Silhouetted soldiers raising an American flag at sunset"></div>
  <h1 class="hero-title">Donate your car to a vet,<br>make a difference.</h1>

  <section class="form-panel">
    <h2>Donate Your Car</h2>
    <p class="lead">Full Tax Deduction - Running or Not<br>Please fill out form or Call toll-free<br>1-800-555-0142</p>
    <div class="fields">
      <div class="field wide">Full Name</div>
      <div class="field">Daytime Phone</div>
      <div class="field">Email</div>
      <div class="field wide">Pickup Address Line 1</div>
      <div class="field wide">Pickup Address Line 2</div>
      <div class="field wide">Pickup City</div>
      <div class="field">Pickup State<span class="caret"></span></div>
      <div class="field">Zip Code</div>
    </div>
    <div class="donate-btn">Donate Now</div>
  </section>

  <section class="panel steps">
    <h2>How To Donate</h2>
    <div class="step" style="left:115px"><div class="step-disc"><span role="img" aria-label="Cordless phone illustration"></span></div><p>Call us 1-800-555-0142<br>or fill out the form</p></div>
    <div class="step" style="left:405px"><div class="step-disc"><span role="img" aria-label="Red tow truck illustration"></span></div><p>We tow it</p></div>
    <div class="step" style="left:695px"><div class="step-disc"><span role="img" aria-label="Tax form with pen illustration"></span></div><p>Tax write-off</p></div>
  </section>

  <section class="panel reasons">
    <h2>Why Donate Your Cars To Us?</h2>
    <ul>
      <li><svg class="arrow-dot" viewBox="0 0 26 26"><circle cx="13" cy="13" r="12" fill="#e11f26" stroke="#f4b0b2" stroke-width="2"/><path d="M7 13h11M13 8l5 5-5 5" stroke="#fff" stroke-width="2.4" fill="none"/></svg><span><b>Top Rated Charity &amp; IRS 501(c)3 Approved :</b> Free 24/7 Pickup with No DMV Hassles.</span></li>
      <li><svg class="arrow-dot" viewBox="0 0 26 26"><circle cx="13" cy="13" r="12" fill="#e11f26" stroke="#f4b0b2" stroke-width="2"/><path d="M7 13h11M13 8l5 5-5 5" stroke="#fff" stroke-width="2.4" fill="none"/></svg><span><b>Free Local Towing :</b> We will pick up your car donation, running or not, when it's most convenient, at home or work.</span></li>
      <li><svg class="arrow-dot" viewBox="0 0 26 26"><circle cx="13" cy="13" r="12" fill="#e11f26" stroke="#f4b0b2" stroke-width="2"/><path d="M7 13h11M13 8l5 5-5 5" stroke="#fff" stroke-width="2.4" fill="none"/></svg><span><b>All Cars Accepted :</b> We take your car regardless of its condition or registration status.</span></li>
      <li><svg class="arrow-dot" viewBox="0 0 26 26"><circle cx="13" cy="13" r="12" fill="#e11f26" stroke="#f4b0b2" stroke-width="2"/><path d="M7 13h11M13 8l5 5-5 5" stroke="#fff" stroke-width="2.4" fill="none"/></svg><span><b>Income Tax Deduction :</b> We issue you an IRS tax receipt &amp; offer the largest resale network to get you the highest tax write-off possible.</span></li>
      <li><svg class="arrow-dot" viewBox="0 0 26 26"><circle cx="13" cy="13" r="12" fill="#e11f26" stroke="#f4b0b2" stroke-width="2"/><path d="M7 13h11M13 8l5 5-5 5" stroke="#fff" stroke-width="2.4" fill="none"/></svg><span><b>No Paperwork Hassles :</b> We take any car and handle everything: DMV, Smog and IRS paperwork.</span></li>
      <li><svg class="arrow-dot" viewBox="0 0 26 26"><circle cx="13" cy="13" r="12" fill="#e11f26" stroke="#f4b0b2" stroke-width="2"/><path d="M7 13h11M13 8l5 5-5 5" stroke="#fff" stroke-width="2.4" fill="none"/></svg><span><b>Car donations help fund programs :</b> And benefit National Heroes Support Fund. An IRS 501(c)3 nonprofit organization.</span></li>
      <li><svg class="arrow-dot" viewBox="0 0 26 26"><circle cx="13" cy="13" r="12" fill="#e11f26" stroke="#f4b0b2" stroke-width="2"/><path d="M7 13h11M13 8l5 5-5 5" stroke="#fff" stroke-width="2.4" fill="none"/></svg><span><b>Schedule a Free Pickup :</b> Complete the form and a representative will call you to arrange a convenient time to pickup your car.</span></li>
    </ul>
  </section>

  <section class="panel today">
    <h2>Donate Your Car Today</h2>
    <div class="perk" style="left:14px"><div class="perk-disc"><div><svg width="80" height="80" viewBox="0 0 80 80"><path d="M66 30A28 28 0 1 1 52 15" stroke="#fff" stroke-width="7" fill="none"/><path d="M24 40l12 12 30-30" stroke="#fff" stroke-width="8" fill="none"/></svg></div></div><p>You have no costs.</p></div>
    <div class="perk" style="left:224px"><div class="perk-disc"><div><svg width="86" height="70" viewBox="0 0 86 70"><rect x="28" y="18" width="40" height="34" rx="6" fill="#fff"/><path d="M28 30L6 8" stroke="#fff" stroke-width="5"/><path d="M6 8v16" stroke="#fff" stroke-width="4"/><rect x="4" y="40" width="30" height="12" fill="#fff"/><circle cx="20" cy="56" r="9" fill="#fff" stroke="#1d4aa3" stroke-width="3"/><circle cx="58" cy="56" r="9" fill="#fff" stroke="#1d4aa3" stroke-width="3"/></svg></div></div><p>Free towing, running<br>or not.</p></div>
    <div class="perk" style="left:435px"><div class="perk-disc"><div><svg width="60" height="80" viewBox="0 0 60 80"><path d="M6 4h48v68l-8-6-8 6-8-6-8 6-8-6-8 6z" stroke="#fff" stroke-width="4" fill="none"/><path d="M14 24h10M14 36h10M32 48h14M32 58h14" stroke="#fff" stroke-width="3"/><text x="34" y="40" fill="#fff" font-family="Open Sans, sans-serif" font-weight="700" font-size="20">$</text></svg></div></div><p>We issue you an<br>IRS tax receipt.</p></div>
    <div class="perk" style="left:646px"><div class="perk-disc"><div><svg width="80" height="80" viewBox="0 0 80 80"><path d="M26 10h38v56H26" stroke="#fff" stroke-width="4" fill="none"/><path d="M40 24h16M44 34h12M44 44h12M40 56h16" stroke="#fff" stroke-width="3"/><circle cx="26" cy="40" r="14" stroke="#fff" stroke-width="5" fill="#1d4aa3"/><path d="M26 33v9M26 45v2" stroke="#fff" stroke-width="4"/><path d="M16 50L6 62" stroke="#fff" stroke-width="7"/></svg></div></div><p>We take care of<br>all paperwork.</p></div>
    <div class="perk" style="left:854px"><div class="perk-disc"><div><svg width="60" height="80" viewBox="0 0 60 80"><rect x="6" y="10" width="48" height="64" rx="3" stroke="#fff" stroke-width="4" fill="none"/><rect x="20" y="4" width="20" height="12" rx="2" fill="#fff"/><rect x="16" y="26" width="28" height="14" rx="4" fill="#fff"/><path d="M14 50h32M14 58h32M14 66h20" stroke="#fff" stroke-width="3"/></svg></div></div><p>We take care of<br>DMV &amp; Smog issues.</p></div>
    <h2 class="secure-title">Safe &amp; Secure</h2>
    <div class="badges">
      <div class="badge-rect" role="img" aria-label="Accredited business rating badge"></div>
      <div class="badge-round" role="img" aria-label="Approved charity seal"></div>
      <div class="badge-shield" role="img" aria-label="Secure site badge"></div>
    </div>
  </section>

  <footer class="footer">
    <div class="foot-about">
      <h3>About Rides For Heroes</h3>
      <p>Lorem ipsum dolor sit amet, consectetuer adipiscing elit, sed diam nonummy nibheu ismod tincidunt ut laoreet dolore magna aliquam erat volutpat. Ut wisi enim ad mini veniam, quis nostrud exerci tation ullamcor per suscipit lobortis nisl ut aliquip ex ea co modo consequat.</p>
    </div>
    <div class="foot-nav">
      <h3>Navigation</h3>
      <a href="#">How To Donate</a><a href="#">Why Donate</a><a href="#">Faq</a><a href="#">About</a>
    </div>
    <div class="foot-contact">
      <h3>Contact Info</h3>
      <div class="line"><svg width="18" height="16" viewBox="0 0 18 16"><path d="M1 5c0-3 16-3 16 0v2h-4V5H5v2H1z" fill="#fff"/><path d="M4 8h10l2 7H2z" fill="#fff"/></svg><span>CALL 1-800-555-0142<br>Live Operators Available<br>7 Days A Week</span></div>
    </div>
    <div class="foot-brand"><span class="brand-dot"></span><span class="brand-name">Rides For Heroes</span></div>
  </footer>
  <div class="copyright">Copyright © 2016 Rides For Heroes. All rights reserved.</div>
</div>
</body>
</html>
```